Business Card Design Project

We need a Business Card for an Mechanical Engineering firm in Singapore. The design should be Modern & Technical looking, yet eye catching.

Our company deals in Cutting Tools & Machine Accessories for the Manufacturing Industries such as Oil & Gas, Aero Space, etc... For more information on our Company, you can either email me or view our website www.valtrion.com.sg.

We are trying to revamp our image to give our consumers a fresh new perspective to our company, so we welcome all ideas.

Industry/Entity Type

Business

Requirements
Must have
• Must incorporate New Company Logo into the card as shown in Uploaded file.

```html
<!DOCTYPE html>
<html lang="en">
<head>
<meta charset="utf-8">
<title>Valtrion Tools – Business Card</title>
<link rel="stylesheet" href="https://fonts.googleapis.com/css2?family=Questrial&display=swap">
<style>
  :root {
    --page: #eeeeee;
    --card: #ffffff;
    --maroon: #951b32;
    --maroon-soft: #d4b5bf;
    --ink-dark: #3b1a21;
  }
  * { margin: 0; padding: 0; box-sizing: border-box; }
  html, body {
    width: 1200px;
    height: 750px;
    overflow: hidden;
    background: var(--page);
  }
  .card {
    position: absolute;
    left: 75px;
    top: 75px;
    width: 1050px;
    height: 600px;
    background: var(--card);
    overflow: hidden;
    font-family: "Questrial", sans-serif;
  }
  .motif-area {
    position: absolute;
    left: 0;
    top: 75px;
    width: 545px;
    height: 525px;
    border-radius: 0 260px 0 0;
    background: linear-gradient(135deg, var(--maroon) 0%, var(--maroon) 45%, var(--maroon-soft) 100%);
  }
  .brand {
    position: absolute;
    right: 37px;
    top: 170px;
    display: flex;
    align-items: center;
    gap: 14px;
  }
  .brand-mark {
    width: 34px;
    height: 34px;
    border-radius: 50%;
    background: var(--maroon);
  }
  .brand-name {
    font-size: 48px;
    line-height: 1;
    letter-spacing: 1px;
    color: var(--ink-dark);
    text-transform: uppercase;
  }
  .contact {
    position: absolute;
    right: 38px;
    top: 272px;
    text-align: right;
    color: var(--maroon);
    line-height: 1.2;
  }
  .contact-name { font-size: 24px; font-variant: small-caps; }
  .contact-phone { font-size: 27px; }
  .contact-street { font-size: 22px; font-variant: small-caps; }
  .contact-city { font-size: 24px; text-transform: uppercase; }
</style>
</head>
<body>
  <main class="card">
    <div class="motif-area" role="img" aria-label="Large interlocking gear decoration in maroon with soft pink offset shadows"></div>

    <div class="brand">
      <span class="brand-name">Valtrion Tools</span>
      <span class="brand-mark"></span>
    </div>

    <address class="contact" style="font-style: normal;">
      <p class="contact-name">Daniel Koh</p>
      <p class="contact-phone">654-210-3987</p>
      <p class="contact-street">48 Kestrel Street</p>
      <p class="contact-city">Singapore 608512</p>
    </address>
  </main>
</body>
</html>
```